Short video intro graphic animation featuring brand mark

I would like a new branded video intro graphic animation to place at the start of the videos I make.
Look at some of the videos on this page for example.
https://www.grovantfield.com/video#!
A more simple one is featured here;
https://www.clipvarno.com/watch?v=Qm7pwrTbN3c
I would like you use white purple and opacity in the graphic.
My logo is simply the text mark in the attachment.
I would like there to be movement as well. It should be quick.
It can include a sound if you like.
The rest is up to you.

```html
<!DOCTYPE html>
<html lang="en">
<head>
<meta charset="utf-8">
<title>Vexlo – Video Intro Title Card</title>
<link rel="stylesheet" href="https://fonts.googleapis.com/css2?family=Arimo:wght@700&display=swap">
<style>
  :root {
    --purple-glow: #dca2d6;
    --purple-mid: #b656a8;
    --purple-body: #b04ea2;
    --purple-deep: #8a2a78;
    --purple-shade: rgba(110, 20, 95, 0.35);
    --white: #ffffff;
  }
  html, body {
    margin: 0;
    padding: 0;
    width: 1200px;
    height: 675px;
    overflow: hidden;
    background: var(--purple-deep);
  }
  .intro-card {
    position: relative;
    width: 1200px;
    height: 675px;
    overflow: hidden;
  }
  .backdrop {
    position: absolute;
    inset: 0;
    background:
      radial-gradient(ellipse 900px 700px at 560px 60px, transparent 55%, var(--purple-shade) 100%),
      radial-gradient(ellipse 720px 560px at 560px 20px, var(--purple-glow) 0%, var(--purple-mid) 55%, transparent 100%),
      linear-gradient(180deg, var(--purple-body) 0%, var(--purple-deep) 100%);
  }
  .brand-name {
    position: absolute;
    left: 542px;
    top: 236px;
    margin: 0;
    font-family: "Arimo", Arial, sans-serif;
    font-weight: 700;
    font-size: 176px;
    line-height: 1;
    letter-spacing: -2px;
    color: var(--white);
    z-index: 2;
  }
  .brand-rule {
    position: absolute;
    left: 575px;
    top: 427px;
    width: 625px;
    height: 7px;
    background: var(--white);
    z-index: 2;
  }
</style>
</head>
<body>
  <main class="intro-card">
    <div class="backdrop" role="img" aria-label="Soft purple glow background with faint translucent square tiles"></div>
    <h1 class="brand-name">Vexlo</h1>
    <div class="brand-rule"></div>
  </main>
</body>
</html>
```